Downloadable PDF "Brochure?"

We have a Free download we will provide in exchange for an email address on our new Trailmark website. The website at www.venturetrailmark-example.com is in development and will look nothing like what it currently does, but you can go there and get a sense of what Trailmark is from the text on the website. (see the attached image 'site design' for the new redesigned website for aesthetics).

We are looking for a nice design for the document, that will represent the mostly text document well. We are not actually looking to print these at a printer so they don't have to be print ready. I went ahead and included the logo and colors and fonts file again just for reference.

Target Market(s)

Business Owners / Decision Makers

Requirements
Must have
• See attached document 'trailmark freebie' for text to be utilized in the finished deliverable.
• See the attached image 'Site Design' for the website aesthetic.

```html
<!DOCTYPE html>
<html lang="en">
<head>
<meta charset="utf-8">
<title>10 Questions to Choose the Best Technology Advisor – Trailmark</title>
<link href="https://fonts.googleapis.com/css2?family=Bebas+Neue&family=Cinzel:wght@600&family=Open+Sans:wght@300;400;600;700&display=swap" rel="stylesheet">
<style>
:root{
  --backdrop:#3b3b3b;
  --paper:#ffffff;
  --copper:#c97b4c;
  --copper-deep:#b8693a;
  --slate:#3a4a52;
  --ink:#3c3c3c;
  --mist:#e6e7e8;
  --panel-text:#fbe6d8;
}
*{margin:0;padding:0;box-sizing:border-box}
html,body{width:1200px;height:850px;overflow:hidden;background:var(--backdrop)}
body{position:relative;font-family:"Open Sans",sans-serif;color:var(--ink)}
.page-label{position:absolute;top:28px;color:#fff;font-weight:700;font-size:19px;font-family:"Open Sans",sans-serif}
.page-label--back{left:66px}
.page-label--front{left:1075px}
.sheet{position:absolute;top:68px;width:526px;height:742px;background:var(--paper);box-shadow:0 3px 8px rgba(0,0,0,.45);overflow:hidden}
.sheet--back{left:62px}
.sheet--front{left:615px}

/* back page */
.column{position:absolute;top:26px;overflow:hidden}
.column--left{left:22px;width:265px}
.column--right{left:304px;width:200px}
.qa h2{font-size:8.4px;line-height:1.45;font-weight:700;color:var(--copper-deep);margin-bottom:5px}
.qa p{font-size:6.75px;line-height:1.57;text-align:justify;margin-bottom:14px;font-weight:400}
.footer-band{position:absolute;left:0;bottom:0;width:100%;height:36px;display:flex;background:var(--copper)}
.footer-band span{display:flex;align-items:center;color:#fff;height:100%;padding-left:22px}
.footer-site{width:202px;font-family:"Cinzel",serif;font-weight:600;font-size:10.6px;letter-spacing:.6px}
.footer-mail{width:206px;border-left:2px solid #fff;border-right:2px solid #fff;padding-left:10px!important;font-weight:700;font-size:9.6px}
.footer-phone{padding-left:10px!important;font-weight:700;font-size:10px}

/* front page */
.hero-title{position:absolute;left:29px;top:32px;font-family:"Bebas Neue",sans-serif;font-size:44px;line-height:42px;color:var(--copper);letter-spacing:.5px}
.hero-title .lead{color:var(--slate)}
.intro-panel{position:absolute;left:289px;top:0;width:237px;height:742px;background:var(--copper);border-left:3px solid var(--mist)}
.intro-panel p{position:absolute;left:25px;top:33px;width:198px;font-size:7.8px;line-height:14.9px;color:var(--panel-text);font-weight:300}
.brand-disc{position:absolute;left:240px;top:193px;width:298px;height:298px;border-radius:50%;background:#fff;border:7px solid var(--mist)}
.brand-name{position:absolute;left:297px;top:320px;display:flex;align-items:center;gap:8px;font-family:"Open Sans",sans-serif;font-weight:600;font-size:25px;letter-spacing:2px;color:var(--slate)}
.brand-name i{display:block;width:20px;height:20px;border-radius:50%;background:var(--copper)}
.feature{position:absolute;left:29px;top:216px;width:242px}
.feature h2{font-size:8.6px;line-height:1.5;font-weight:700;color:var(--copper-deep);margin-bottom:8px}
.feature p{font-size:6.9px;line-height:1.66;text-align:justify}
.photo{position:absolute}
.photo--advisor{left:0;top:478px;width:290px;height:264px;background:linear-gradient(180deg,#ffffff 0%,#e4e4e4 45%,#9c9c9c 100%)}
.photo--meeting{left:305px;top:480px;width:194px;height:119px;background:linear-gradient(135deg,#6b5445,#b89a80 55%,#d9cfc4)}
.photo--stairs{left:305px;top:610px;width:194px;height:119px;background:linear-gradient(135deg,#cfcfcf,#a9a9a9 60%,#8a8a8a)}
.front-site{position:absolute;left:29px;top:705px;font-family:"Cinzel",serif;font-weight:600;font-size:13.6px;color:#fff;letter-spacing:.4px}
</style>
</head>
<body>
<div class="page-label page-label--back">Page 2</div>
<div class="page-label page-label--front">Page 1</div>

<section class="sheet sheet--back">
  <div class="column column--left">
    <article class="qa">
      <h2>Provide an example where you solved a problem without the use of technology?</h2>
      <p>Often technology-minded individuals become so wrapped up in the solutions themselves they fail to realize a policy or process change is far more effective and simple than making changes to existing or introducing new technology. Asking for a specific example here should demonstrate the ability to think from a business mindset. For specific examples reference ‘The Firebird Initiative’ by Lane, Moreau, and Pratt.</p>
    </article>
    <article class="qa">
      <h2>How do you go about prioritizing solutions in order of importance for implementation / adoption?</h2>
      <p>Answers here should include reference to some form of discovery process or a thorough evaluation at the operations level. One of the key skill sets for someone approaching technology from a business point of view is mapping solutions and their respective importance to business outcomes and (often more importantly) eliminating bottlenecks while respecting that some implementations must necessarily come before others to be viable. For reference on the Theory of Constraints see ‘The Bottleneck’ by Idris Kalman.</p>
    </article>
    <article class="qa">
      <h2>What is Information Technology Debt?</h2>
      <p>Stated simply, ‘IT Debt’ is a measurement of the out-of-date, incomplete or yet-to-be-defined technology changes. Debt occurs for a number of reasons, including lack of qualified personnel to implement the needed solutions (or recognize the problem in the first place); historical spending haunting the organization “we spent money on something like this before and look what it got us”; Fire-fighting (addressing issues purely reactively in a downward spiral leaving no time for fixing the real underlying problem); or most commonly, the budget being already allocated to other company endeavors that seem immediately more pressing. By recognizing what IT Debt is, the individual demonstrates an acknowledgment of how impactful it can be when neglected and not brought to the forefront of business planning sessions.</p>
    </article>
    <article class="qa">
      <h2>Provide an example where you argued against implementing a technology solution and why?</h2>
      <p>Despite it being seemingly obvious, using ‘outside of budget’ is not a good answer. Business-minded technology advisors should be intimately aware of how well a proposed solution will integrate into the existing company ecosystem (software tools already present, workflow, and processes), if it drives the company toward reducing/eliminating a bottleneck (and thereby creates more leverage), and if it fits the company’s culture. If any of these are a no, the solution should be carefully examined for what it really offers the organization. If yes, the budget should be evaluated as a cost-benefit analysis, not a flat number ‘not to exceed’.</p>
    </article>
    <article class="qa">
      <h2>What is your ideal method for maintaining technology alignment for the company?</h2>
      <p>You want to see a specific process envisioned here. At the very least a recommendation to be involved in business planning meetings or retreats, and ideally a standing technology focused meeting with leadership present should be argued for. For technology to be truly in alignment, it must fit the needs of the organization, not the other way around. This needs to come from the top level, and it means a representative must be present in critical business strategy meetings to understand where the company is headed, what operational constraints they are encountering, and what their short-term goals are. For an outline of how this model has been the underlying key to success for several well-known companies reference ‘Solid to Superb’ by Jonah Fell.</p>
    </article>
  </div>
  <div class="column column--right">
    <article class="qa">
      <h2>How do you plan on measuring and monitoring the adoption success of a solution or project?</h2>
      <p>Technically minded individuals often look at the point of ‘it’s up and running and it all works’, as where their responsibilities end. Someone with a business mindset should demonstrate that evaluating how well the solution has been adopted into the day to day workflow, and to what degree the solution has increased leverage or operational transparency are the true critical indicators of success. There should be a specific process of follow-up after implementation to flag adoption or workflow issues due to problems such as inadequate training, unforeseen incompatibilities (whether they be process or technology related), or simply resistance to change. These findings can then be brought back to leadership to evaluate how best to improve successful adoption going forward.</p>
    </article>
    <article class="qa">
      <h2>Provide an example where you had to balance customer and employee technology experience with security and compliance?</h2>
      <p>A critical role fulfilled by a technology advisor is being able to balance maintaining compliance and sound security practices with as painless of a technology experience as possible. They should be able to weigh the critical importance of protecting the organization from the negative public relations and liability of a security flaw while respecting a solution must be usable to be useful. Look for an example that demonstrates an understanding of both sides and strikes a balance without going to an extreme in either direction.</p>
    </article>
    <article class="qa">
      <h2>What would you do first, if you were selected as our advisor? Can you give me details on what your discovery or on-boarding process includes?</h2>
      <p>You are looking to make sure that they don’t stop at the technology. There should be a higher focus on understanding what the company processes are and how the people inside the organization get work done. If they focus only on network, security, and disaster recovery assessments then they do not have a business mindset.</p>
    </article>
    <article class="qa">
      <h2>Can you give me an example of a time you gave a suggestion for a solution and it was not taken? Describe the solution and why it was important to the organization. And why do you think they didn’t implement it?</h2>
      <p>When they describe why they think the solution was important do they simply talk about risk reduction or uptime improvements without tying them back to an organizational goal or bottleneck. Being able to demonstrate actual business value is a critical skill for a technology advisor. For reference on technical excellence in service of business objectives rather than blindly servicing requirements see ‘A Chair at The Board’ by Reed Calloway.</p>
    </article>
  </div>
  <footer class="footer-band">
    <span class="footer-site">VENTURETRAILMARK-EXAMPLE.COM</span>
    <span class="footer-mail">hello@venturetrailmark-example.com</span>
    <span class="footer-phone">(555) 010-0147</span>
  </footer>
</section>

<section class="sheet sheet--front">
  <div class="photo photo--advisor" role="img" aria-label="Photo of a businessman in a suit looking up at a rising arrow"></div>
  <div class="intro-panel">
    <p>When you choose a technology advisor whether it be a Managed Service Provider, fractional CIO or a full-time CIO you need to make sure that they understand business just as much as they understand technology. Some of the biggest complaints about the IT department are that they just don’t “Get it”. The questions below should help you determine whether or not they have a technology mindset or a business mindset.</p>
  </div>
  <div class="brand-disc"></div>
  <div class="brand-name"><i></i>TRAILMARK</div>
  <h1 class="hero-title"><span class="lead">10 Questions</span> to<br>Choose the Best<br>Technology<br>Advisor</h1>
  <article class="feature">
    <h2>What is scalability? How important is it from a technology perspective on a scale of 1-&gt;10 with 10 being the highest? What all does scalability impact?</h2>
    <p>This question is designed to get a reading on the person’s mindset. A typical technology-minded response would be something describing the ability of systems or software to scale by adding additional resources. When working from a business point of view, however, you want to see it defined as the ability for the organization to support increased volume without sacrificing margins. The importance of this concept cannot be overstated and should be a 9 or 10 in terms of ranking. Regarding impact, you want to see not just an understanding of having to spend money two or three times for a different solution to the same problem, but an acknowledgment of the ‘total’ cost, including adoption fatigue, the opportunity cost of change, and the competitive disadvantage it creates. For concepts of business scalability refer to ‘Growing Up’ by Dale Harker.</p>
  </article>
  <div class="photo photo--meeting" role="img" aria-label="Photo of an advisor meeting with a couple at a café table"></div>
  <div class="photo photo--stairs" role="img" aria-label="Photo of a businessman climbing steps labelled idea, plan, team, business, success"></div>
  <div class="front-site">VENTURETRAILMARK-EXAMPLE.COM</div>
</section>
</body>
</html>
```